Velmin & Co Powerpoint Template

A simple powerpoint template for my business which provides management consulting services for Business Owners.

It should reflect the colours within the logo design and should work as the master template for all standard powerpoint slide layouts.

```html
<!DOCTYPE html>
<html lang="en">
<head>
<meta charset="utf-8">
<title>Velmin &amp; Co – Presentation Template</title>
<link rel="stylesheet" href="https://fonts.googleapis.com/css2?family=Poppins:wght@600;700&family=Roboto:wght@300;400;500;700&display=swap">
<style>
:root{
  --orange:#e2561d;
  --orange-soft:#f07a3e;
  --ink:#0d0d0d;
  --text:#555555;
  --white:#ffffff;
  --page:#fdf3ef;
  --mint:#eef6f4;
  --dark2:#0f0f0f;
}
*{box-sizing:border-box;margin:0;padding:0}
html,body{width:1200px;height:4051px;overflow:hidden}
body{background:var(--page);font-family:'Roboto',sans-serif;position:relative}
.slide{position:absolute;left:75px;width:1048px;height:590px;background:var(--white);overflow:hidden;box-shadow:0 4px 14px rgba(0,0,0,.06)}
.slide--dark{background:var(--dark2)}
.slide--mint{background:var(--mint)}
.photo-backdrop{position:absolute;inset:0;background:linear-gradient(110deg,#3a3a3a 0%,#1c1c1c 45%,#111 100%)}

/* brand tab */
.brand-tab{position:absolute;right:0;top:0;width:279px;height:107px;background:var(--ink);border-left:7px solid var(--orange);border-bottom:7px solid var(--orange);border-bottom-left-radius:110px 107px;display:flex;flex-direction:column;align-items:center;justify-content:center;padding-left:30px;color:var(--white)}
.brand-tab--light{background:var(--mint);color:var(--ink)}
.brand-row{display:flex;align-items:center;gap:10px}
.brand-dot{width:22px;height:22px;border-radius:50%;background:var(--orange)}
.brand-name{font-size:17px;line-height:17px;font-weight:400;border-left:1px solid currentColor;padding-left:10px}
.brand-tag{font-size:8px;margin-top:6px}

/* headings */
.slide-title{position:absolute;left:60px;top:22px;font-family:'Poppins',sans-serif;font-weight:700;font-size:42px;color:var(--ink);letter-spacing:.2px}
.slide-title span{color:var(--orange)}
.title-rule{position:absolute;left:0;top:88px;width:134px;height:3px;background:var(--orange)}
.title-rule::after{content:"";position:absolute;right:-3px;top:-4px;width:11px;height:11px;border-radius:50%;background:var(--orange)}

/* footer */
.footer-rule{position:absolute;left:0;right:0;top:559px;height:2px;background:var(--orange)}
.page-num{position:absolute;left:956px;top:544px;width:32px;height:32px;border-radius:50%;background:var(--orange);color:var(--white);font-size:12px;display:flex;align-items:center;justify-content:center}

.body-copy{font-size:14.5px;line-height:25px;color:var(--text);text-align:justify}
.img-fill{position:absolute;border-radius:20px}

/* slide 1 */
.cover-title{position:absolute;left:461px;top:205px;font-family:'Poppins',sans-serif;font-weight:600;font-size:44px;color:var(--white)}
.cover-sub{position:absolute;left:461px;top:265px;font-size:32px;font-weight:300;color:var(--orange-soft)}
.cover-text{position:absolute;left:461px;top:327px;width:527px;font-size:14.5px;line-height:25px;color:var(--white);text-align:justify}

/* slide 2 */
.about-text{position:absolute;left:60px;top:185px;width:410px}
.about-text p+p{margin-top:13px}

/* slide 3 */
.service-card{position:absolute;top:156px;width:277px;height:355px;background:var(--white);border-radius:10px;box-shadow:0 2px 12px rgba(226,86,29,.15);padding:6px;text-align:center}
.service-photo{height:197px;border-radius:6px 6px 0 0}
.service-name{margin-top:28px;font-size:15px;font-weight:500;color:var(--ink)}
.service-text{margin:12px 18px 0;font-size:14px;line-height:23px;color:var(--text)}

/* slide 4 */
.benefit-list{position:absolute;left:577px;top:186px;width:411px;list-style:none}
.benefit-list li{position:relative;padding-left:37px;margin-bottom:14px;font-size:14.5px;line-height:25px;color:var(--text);text-align:justify}
.benefit-list li::before{content:"";position:absolute;left:0;top:7px;width:12px;height:12px;border:2px solid var(--orange);border-radius:50%}
.benefit-list li::after{content:"";position:absolute;left:4px;top:12px;width:6px;height:2px;background:var(--orange)}

/* slide 5 */
.diagram{position:absolute;left:0;top:0}
.point{position:absolute;width:170px}
.point h3{font-size:14px;font-weight:700;color:var(--ink);margin-bottom:6px}
.point p{font-size:10px;line-height:15px;color:#777}
.point--left{text-align:right}
.point--top{text-align:center;width:230px}
.hub-name{position:absolute;left:424px;top:378px;width:200px;text-align:center;font-size:20px;color:var(--orange)}

/* slide 6 */
.thanks-title{position:absolute;left:461px;top:134px;font-family:'Poppins',sans-serif;font-weight:700;font-size:48px;color:var(--white)}
.thanks-title span{color:var(--orange)}
.contact{position:absolute;left:461px;display:flex;align-items:flex-start;gap:30px;color:var(--white);font-size:17px;line-height:25px}
.contact svg{flex:0 0 28px;margin-top:-1px}
</style>
</head>
<body>

<!-- Cover -->
<section class="slide slide--dark" style="top:87px">
  <div class="photo-backdrop" role="img" aria-label="Dimmed photo of business people meeting at a desk"></div>
  <div class="brand-tab brand-tab--light">
    <div class="brand-row"><div class="brand-dot"></div><div class="brand-name">Velmin<br>&amp; Co</div></div>
    <div class="brand-tag">Supporting Business Owners</div>
  </div>
  <h1 class="cover-title">Velmin &amp; Co</h1>
  <p class="cover-sub">Supporting Business Owners</p>
  <p class="cover-text">Lorem ipsum dolor sit amet, consectetur adipiscing elit, sed do eiusmod tempor incididunt ut labore et dolore magna aliqua.</p>
  <div class="footer-rule"></div><div class="page-num">1</div>
</section>

<!-- About -->
<section class="slide" style="top:744px">
  <h2 class="slide-title">About <span>Us</span></h2><div class="title-rule"></div>
  <div class="brand-tab">
    <div class="brand-row"><div class="brand-dot"></div><div class="brand-name">Velmin<br>&amp; Co</div></div>
    <div class="brand-tag">Supporting Business Owners</div>
  </div>
  <div class="about-text body-copy">
    <p>Lorem ipsum dolor sit amet, consectetur adipiscing elit, sed do eiusmod tempor incididunt ut labore et dolore magna aliqua. Ut enim ad minim veniam, quis nostrud exercitation ullamco laboris nisi ut aliquip ex ea commodo consequat. Duis aute irure dolor in reprehenderit in voluptate velit esse cillum dolore eu fugiat nulla pariatur.</p>
    <p>Lorem ipsum dolor sit amet, consectetur adipiscing elit, sed do eiusmod tempor incididunt ut labore et dolore magna aliqua. Ut enim ad minim veniam, quis nostrud exercitation ullamco laboris nisi ut aliquip ex ea commodo consequat. Duis aute irure dolor in reprea.</p>
  </div>
  <div class="img-fill" style="left:524px;top:151px;width:464px;height:360px;background:linear-gradient(135deg,#d9dde0,#8c949a 55%,#3a3f44)" role="img" aria-label="Photo of two colleagues reviewing a tablet in an office"></div>
  <div class="footer-rule"></div><div class="page-num">2</div>
</section>

<!-- Services -->
<section class="slide" style="top:1401px">
  <h2 class="slide-title">Our <span>Services</span></h2><div class="title-rule"></div>
  <div class="brand-tab">
    <div class="brand-row"><div class="brand-dot"></div><div class="brand-name">Velmin<br>&amp; Co</div></div>
    <div class="brand-tag">Supporting Business Owners</div>
  </div>
  <article class="service-card" style="left:61px">
    <div class="service-photo" style="background:linear-gradient(135deg,#c9a27c,#6e5646)" role="img" aria-label="Photo of two people talking in a lounge"></div>
    <h3 class="service-name">LORUM IPSUM DOL</h3>
    <p class="service-text">Lorem ipsum dolor sit amet, conse ctetur adipiscing elit, sed do eiu smod tempor incidie.</p>
  </article>
  <article class="service-card" style="left:366px">
    <div class="service-photo" style="background:linear-gradient(135deg,#8fa3ad,#2f3e46)" role="img" aria-label="Photo of a smiling woman at a meeting table"></div>
    <h3 class="service-name">LORUM IPSUM DOL</h3>
    <p class="service-text">Lorem ipsum dolor sit amet, conse ctetur adipiscing elit, sed do eiu smod tempor incidie.</p>
  </article>
  <article class="service-card" style="left:671px">
    <div class="service-photo" style="background:linear-gradient(135deg,#dfe4e2,#7c8a86)" role="img" aria-label="Photo of a group workshop in a bright room"></div>
    <h3 class="service-name">LORUM IPSUM DOL</h3>
    <p class="service-text">Lorem ipsum dolor sit amet, conse ctetur adipiscing elit, sed do eiu smod tempor incidie.</p>
  </article>
  <div class="footer-rule"></div><div class="page-num">3</div>
</section>

<!-- Benefits -->
<section class="slide" style="top:2058px">
  <h2 class="slide-title">Our <span>Benefits</span></h2><div class="title-rule"></div>
  <div class="brand-tab">
    <div class="brand-row"><div class="brand-dot"></div><div class="brand-name">Velmin<br>&amp; Co</div></div>
    <div class="brand-tag">Supporting Business Owners</div>
  </div>
  <div class="img-fill" style="left:61px;top:151px;width:463px;height:360px;background:linear-gradient(135deg,#b49a86,#5b4a40 55%,#2e2a28)" role="img" aria-label="Photo of a team working together over papers at a table"></div>
  <ul class="benefit-list">
    <li>Lorem ipsum dolor sit amet, consectetur adipiscing elit, sed do eiusmod tempor incididunt ut labore et dolore magna aliqu enim ad minim.</li>
    <li>Lorem ipsum dolor sit amet, consectetur adipiscing elit, sed do eiusmod tempor incididunt ut lab.</li>
    <li>Lorem ipsum dolor sit amet, consectetur adipiscing elit, sed do eiusmod tempor incididunt ut labore et dolore magna aliqu enim ad minim.</li>
    <li>Lorem ipsum dolor sit amet, consectetur adipiscing elit, sed do eiusmod tempor incididunt ut lab.</li>
  </ul>
  <div class="footer-rule"></div><div class="page-num">4</div>
</section>

<!-- Why choose us -->
<section class="slide slide--mint" style="top:2715px">
  <h2 class="slide-title">Why <span>Choose Us</span></h2><div class="title-rule"></div>
  <div class="brand-tab">
    <div class="brand-row"><div class="brand-dot"></div><div class="brand-name">Velmin<br>&amp; Co</div></div>
    <div class="brand-tag">Supporting Business Owners</div>
  </div>
  <svg class="diagram" width="1048" height="590" viewBox="0 0 1048 590" aria-hidden="true">
    <g fill="none" stroke="#e2561d" stroke-width="1.5">
      <circle cx="524" cy="393" r="122"/>
      <line x1="524" y1="241" x2="524" y2="271"/>
      <polyline points="340,299 382,299 419,330"/>
      <polyline points="340,488 382,488 419,457"/>
      <polyline points="707,299 666,299 629,330"/>
      <polyline points="707,485 666,485 629,457"/>
    </g>
    <g fill="#fff" stroke="#e2561d" stroke-width="1.5">
      <circle cx="524" cy="271" r="4"/><circle cx="419" cy="330" r="4"/><circle cx="419" cy="457" r="4"/><circle cx="629" cy="330" r="4"/><circle cx="629" cy="457" r="4"/>
    </g>
    <circle cx="524" cy="393" r="102" fill="#0d0d0d"/>
    <g fill="#e2561d" stroke="#fff" stroke-width="4">
      <circle cx="524" cy="209" r="32"/>
      <circle cx="308" cy="299" r="32"/>
      <circle cx="308" cy="488" r="32"/>
      <circle cx="739" cy="299" r="32"/>
      <circle cx="739" cy="485" r="32"/>
    </g>
    <g fill="none" stroke="#fff" stroke-width="1.6" stroke-linecap="round" stroke-linejoin="round">
      <rect x="512" y="199" width="24" height="17" rx="2"/><line x1="519" y1="221" x2="529" y2="221"/><circle cx="524" cy="207" r="4"/>
      <circle cx="310" cy="300" r="9"/><polyline points="306,300 309,303 314,297"/><line x1="296" y1="296" x2="300" y2="296"/><line x1="294" y1="301" x2="299" y2="301"/>
      <rect x="298" y="482" width="10" height="14"/><rect x="310" y="478" width="10" height="18"/><line x1="296" y1="496" x2="322" y2="496"/>
      <rect x="728" y="293" width="14" height="14"/><circle cx="748" cy="292" r="5"/><line x1="735" y1="296" x2="735" y2="304"/>
      <rect x="727" y="478" width="24" height="15" rx="2"/><circle cx="739" cy="485" r="4"/>
    </g>
  </svg>
  <div class="hub-name">Velmin &amp; Co</div>
  <div class="point point--top" style="left:409px;top:112px"><h3>LORUM IPSUM</h3><p>Lorem ipsum dolor sit amet cons ectet adipi scing elit sed do incidid.</p></div>
  <div class="point point--left" style="left:83px;top:264px"><h3>LORUM IPSUM</h3><p>Lorem ipsum dolor sit amet cons ectet adipi scing elit sed do eius mod tempo incidid.</p></div>
  <div class="point point--left" style="left:83px;top:451px"><h3>LORUM IPSUM</h3><p>Lorem ipsum dolor sit amet cons ectet adipi scing elit sed do eius mod tempo incidid.</p></div>
  <div class="point" style="left:794px;top:267px"><h3>LORUM IPSUM</h3><p>Lorem ipsum dolor sit amet cons ectet adipi scing elit sed do eius mod tempo incidid.</p></div>
  <div class="point" style="left:794px;top:451px"><h3>LORUM IPSUM</h3><p>Lorem ipsum dolor sit amet cons ectet adipi scing elit sed do eius mod tempo incidid.</p></div>
  <div class="footer-rule"></div><div class="page-num">5</div>
</section>

<!-- Thank you -->
<section class="slide slide--dark" style="top:3372px">
  <div class="photo-backdrop" role="img" aria-label="Dimmed photo of a laptop on a desk"></div>
  <div class="brand-tab brand-tab--light">
    <div class="brand-row"><div class="brand-dot"></div><div class="brand-name">Velmin<br>&amp; Co</div></div>
    <div class="brand-tag">Supporting Business Owners</div>
  </div>
  <h2 class="thanks-title">Thank <span>You</span></h2>
  <div class="contact" style="top:246px">
    <svg width="28" height="28" viewBox="0 0 24 24" fill="#e2561d"><path d="M6.6 10.8a15 15 0 0 0 6.6 6.6l2.2-2.2c.3-.3.7-.4 1-.2 1.1.4 2.3.6 3.6.6.6 0 1 .4 1 1V20c0 .6-.4 1-1 1A17 17 0 0 1 3 4c0-.6.4-1 1-1h3.5c.6 0 1 .4 1 1 0 1.3.2 2.5.6 3.6.1.3 0 .7-.2 1z"/></svg>
    <span>+1 (555) 014 2290</span>
  </div>
  <div class="contact" style="top:297px">
    <svg width="28" height="28" viewBox="0 0 24 24" fill="none" stroke="#e2561d" stroke-width="2"><circle cx="12" cy="12" r="9"/><line x1="3" y1="12" x2="21" y2="12"/><ellipse cx="12" cy="12" rx="4" ry="9"/></svg>
    <span>https://velminco.com/</span>
  </div>
  <div class="contact" style="top:347px">
    <svg width="28" height="28" viewBox="0 0 24 24" fill="none" stroke="#e2561d" stroke-width="2"><rect x="2" y="5" width="20" height="14"/><polyline points="2,5 12,13 22,5"/></svg>
    <span>info@velminco.com</span>
  </div>
  <div class="contact" style="top:397px">
    <svg width="28" height="28" viewBox="0 0 24 24" fill="#e2561d"><path d="M12 2a7 7 0 0 0-7 7c0 5 7 13 7 13s7-8 7-13a7 7 0 0 0-7-7zm0 9.5A2.5 2.5 0 1 1 12 6.5a2.5 2.5 0 0 1 0 5z"/></svg>
    <span>Lorem ipsum dolor sit consectetur adip elit,<br>United States</span>
  </div>
  <div class="footer-rule"></div><div class="page-num">6</div>
</section>

</body>
</html>
```